Purchasing community for life science startups needs landing page for collecting of contact adresses

We are the "Pipette Union", the first purchasing community for life science startups. The idea is to bundle the needs of several smaller companies (laboratories) and to buy lab consumables and chemicals in larger quantities. This bargaining position, at the end of all participants can buy their products very low prices. In the attached powerpoint file you will find an idea and some elements, which demonstrate a little the style, which came into my mind.
Urlaub/Ferien
Target Market(s)
Our target customers are startups and smaller biotech companies, which are too small to get the best prices. The aim of this landing page is to collect all interested parties.
Look and feel

```html
<!DOCTYPE html>
<html lang="de">
<head>
<meta charset="utf-8">
<title>Pipette Union – Gemeinsam einkaufen</title>
<link href="https://fonts.googleapis.com/css2?family=Montserrat:wght@300;400;600;700;800&family=Lato:wght@300;400;700;900&display=swap" rel="stylesheet">
<style>
  :root {
    --cyan: #1ea8e0;
    --navy: #173f6f;
    --text: #3a4a5c;
    --blue-deep: #2a5bc8;
    --blue-light: #5aa8ea;
    --green-a: #c6df4a;
    --green-b: #aed63a;
    --button-a: #3566cf;
    --button-b: #3f8fe0;
    --footer: #a8acb2;
    --white: #ffffff;
    --kraft-a: #c9a06b;
    --kraft-b: #9c7448;
  }
  * { margin: 0; padding: 0; box-sizing: border-box; }
  html, body { width: 838px; height: 1200px; overflow: hidden; background: var(--white); }
  body { font-family: 'Lato', sans-serif; color: var(--text); position: relative; }
  .abs { position: absolute; }

  /* Brand */
  .brand-mark { left: 205px; top: 30px; width: 95px; height: 95px; background: linear-gradient(180deg, #1f8fe0, #0d4f9a); }
  .brand-name { left: 314px; top: 28px; font-family: 'Montserrat', sans-serif; font-weight: 700; font-size: 35px; letter-spacing: -1px; color: #111; line-height: 1; white-space: nowrap; }
  .brand-tagline { left: 314px; top: 64px; font-family: 'Montserrat', sans-serif; font-weight: 400; font-size: 19px; color: #222; line-height: 1; white-space: nowrap; }

  /* Hero */
  .hero { left: 0; top: 142px; width: 838px; height: 188px; background: radial-gradient(ellipse at 50% 55%, #8fc2f0 0%, var(--blue-light) 30%, var(--blue-deep) 100%); }
  .hero-title { left: 0; top: 190px; width: 838px; text-align: center; font-family: 'Montserrat', sans-serif; font-weight: 800; font-size: 38px; color: var(--white); letter-spacing: 0.5px; line-height: 46px; }
  .hero-sub { left: 0; top: 236px; width: 838px; text-align: center; font-family: 'Montserrat', sans-serif; font-weight: 300; font-size: 35px; color: var(--white); line-height: 44px; }

  /* Question row */
  .question { width: 240px; text-align: center; font-size: 10.5px; line-height: 13px; }
  .question b { color: var(--cyan); font-weight: 700; }
  .question svg { display: block; margin: 0 auto 14px; }

  /* Green band */
  .band { left: 0; top: 463px; width: 838px; height: 107px; background: linear-gradient(90deg, var(--green-a), #d6e96a 50%, var(--green-b)); }
  .band-call { left: 135px; top: 498px; font-weight: 700; font-size: 14.5px; line-height: 19px; color: var(--navy); }
  .band-title { left: 532px; top: 485px; font-family: 'Montserrat', sans-serif; font-weight: 700; font-size: 15px; color: var(--navy); }
  .band-list { left: 523px; top: 508px; list-style: none; font-size: 10.5px; line-height: 13px; color: var(--navy); }

  /* Benefits */
  .product-box { left: 92px; top: 560px; width: 160px; height: 160px; background: linear-gradient(135deg, var(--kraft-a), var(--kraft-b)); transform: skewY(-4deg); box-shadow: 0 6px 10px rgba(0,0,0,0.15); }
  .benefits-title { left: 0; top: 588px; width: 838px; text-align: center; font-family: 'Montserrat', sans-serif; font-weight: 700; font-size: 15px; color: var(--cyan); line-height: 18px; }
  .benefits-intro { left: 0; top: 612px; width: 838px; text-align: center; font-size: 10.5px; line-height: 13px; }
  .benefits-list { top: 653px; left: 0; width: 838px; text-align: center; list-style: none; font-family: 'Montserrat', sans-serif; font-weight: 700; font-size: 11px; color: var(--navy); line-height: 19px; }
  .benefits-list li::before { content: "\25B8  "; font-size: 8px; }

  .cta { width: 218px; height: 27px; line-height: 27px; text-align: center; background: linear-gradient(90deg, var(--button-a), var(--button-b)); color: var(--white); font-weight: 700; font-size: 11px; border-radius: 2px; text-decoration: none; }
  .cta-one { left: 310px; top: 727px; }
  .cta-two { left: 310px; top: 1123px; }
  .mail-icon { left: 548px; top: 723px; }
  .signup-note { left: 0; top: 769px; width: 838px; text-align: center; font-size: 10.5px; line-height: 13px; }

  /* Info sections */
  .info-icon { left: 150px; }
  .info-rule { left: 203px; width: 1px; background: #6a7886; }
  .info { left: 222px; width: 475px; font-size: 10.5px; line-height: 13px; }
  .info h3 { font-family: 'Montserrat', sans-serif; font-weight: 700; font-size: 11px; color: var(--cyan); line-height: 13px; }

  /* Footer */
  .footer { left: 0; top: 1165px; width: 838px; height: 35px; background: var(--footer); }
  .footer-text { left: 148px; top: 1173px; font-size: 6.5px; line-height: 9px; color: var(--white); }
</style>
</head>
<body>

  <div class="abs brand-mark"></div>
  <div class="abs brand-name">PIPETTE UNION</div>
  <div class="abs brand-tagline">Einkaufsverbund Laborbedarf</div>

  <div class="abs hero" role="img" aria-label="Blaue Wasseroberfläche mit Tropfen"></div>
  <h1 class="abs hero-title">GEMEINSAM EINKAUFEN</h1>
  <div class="abs hero-sub">zu Großhandelspreisen</div>

  <div class="abs question" style="left:65px; top:348px;">
    <svg width="50" height="50" viewBox="0 0 50 50" fill="none" stroke="#173f6f" stroke-width="1.6">
      <rect x="5" y="15" width="28" height="28"/><rect x="17" y="5" width="28" height="28"/>
      <line x1="5" y1="15" x2="17" y2="5"/><line x1="33" y1="15" x2="45" y2="5"/>
      <line x1="5" y1="43" x2="17" y2="33"/><line x1="33" y1="43" x2="45" y2="33"/>
      <circle cx="5" cy="15" r="3" fill="#fff"/><circle cx="33" cy="15" r="3" fill="#fff"/>
      <circle cx="5" cy="43" r="3" fill="#fff"/><circle cx="33" cy="43" r="3" fill="#fff"/>
      <circle cx="17" cy="5" r="3" fill="#fff"/><circle cx="45" cy="5" r="3" fill="#fff"/>
      <circle cx="45" cy="33" r="3" fill="#fff"/><circle cx="25" cy="24" r="3" fill="#fff"/>
    </svg>
    <b>Betreibst du</b><br>ein LifeScience Labor?
  </div>

  <div class="abs question" style="left:290px; top:348px;">
    <svg width="66" height="50" viewBox="0 0 66 50" fill="none" stroke="#173f6f" stroke-width="1.6">
      <rect x="2" y="18" width="62" height="26" rx="3"/>
      <path d="M12 6 V34 a4 4 0 0 0 8 0 V6"/><path d="M29 6 V34 a4 4 0 0 0 8 0 V6"/><path d="M46 6 V34 a4 4 0 0 0 8 0 V6"/>
      <line x1="9" y1="6" x2="23" y2="6"/><line x1="26" y1="6" x2="40" y2="6"/><line x1="43" y1="6" x2="57" y2="6"/>
    </svg>
    <b>Benötigst du regelmäßig</b><br>Laborbedarf?
  </div>

  <div class="abs question" style="left:505px; top:346px;">
    <svg width="50" height="52" viewBox="0 0 50 52" fill="none" stroke="#173f6f" stroke-width="1.6">
      <path d="M6 14 L36 3 L42 14"/>
      <rect x="3" y="14" width="44" height="35" rx="3"/>
      <rect x="38" y="26" width="9" height="10" rx="2"/>
      <line x1="7" y1="44" x2="42" y2="44" stroke-dasharray="1.5 1.5"/>
    </svg>
    <b>Würdest du gerne</b><br>für alle Artikel ohne Verhandlung<br>immer den besten Preis erhalten?
  </div>

  <div class="abs band" role="img" aria-label="Grüner Streifen mit feinem Punktmuster"></div>
  <div class="abs band-call">Dann mach mit und werde Teilnehmer der ersten<br>Pipette Union 2019 und spare bis zu 40%.</div>
  <div class="abs band-title">VORTEILE</div>
  <ul class="abs band-list">
    <li>• Kaufe ein zu Großhandelspreisen</li>
    <li>• Keine Verhandlungen mit Lieferanten</li>
    <li>• Keine Vertragsverpflichtung</li>
  </ul>

  <div class="abs product-box" role="img" aria-label="Versandkarton der Einkaufsgemeinschaft"></div>
  <h2 class="abs benefits-title">VORTEILE FÜR TEILNEHMER</h2>
  <p class="abs benefits-intro">Jeder Teilnehmer wird im Prinzip zum Großabnehmer<br>und die Einkaufsgemeinschaft zu deinem guten Einkaufspartner.</p>
  <ul class="abs benefits-list">
    <li>Spare 20 - 40% im Einkauf völlig ohne Verhandlungen</li>
    <li>mehr Zeit für euer Kerngeschäft</li>
    <li>Keine Vertragsverpflichtung</li>
  </ul>

  <a class="abs cta cta-one" href="#">ICH MÖCHTE MEHR ERFAHREN</a>
  <svg class="abs mail-icon" width="102" height="42" viewBox="0 0 102 42" fill="none" stroke="#c9ccd0" stroke-width="2.5">
    <rect x="40" y="3" width="58" height="36"/>
    <path d="M40 3 L69 24 L98 3"/><path d="M40 39 L62 19"/><path d="M98 39 L76 19"/>
    <line x1="10" y1="8" x2="34" y2="8"/><line x1="2" y1="15" x2="34" y2="15"/>
    <line x1="14" y1="22" x2="34" y2="22"/><line x1="6" y1="29" x2="34" y2="29"/><line x1="18" y1="36" x2="34" y2="36"/>
  </svg>
  <p class="abs signup-note">Hast du Interesse an einer Teilnahme?<br>Dann trage dich gerne völlig unverbindlich in unsere<br>Interessentenliste ein, sodass wir Kontakt zu dir aufnehmen können.</p>

  <svg class="abs info-icon" style="top:842px;" width="40" height="42" viewBox="0 0 40 42" fill="none" stroke="#173f6f" stroke-width="1.5">
    <path d="M6 20 L12 12 H28 L34 20 L20 40 Z"/><path d="M6 20 H34"/><path d="M14 20 L20 40 L26 20"/><path d="M12 12 L16 20 L20 12 L24 20 L28 12"/>
    <line x1="20" y1="1" x2="20" y2="7"/><line x1="9" y1="3" x2="12" y2="8"/><line x1="31" y1="3" x2="28" y2="8"/>
  </svg>
  <div class="abs info-rule" style="top:842px; height:80px;"></div>
  <div class="abs info" style="top:842px;">
    <h3>UNSER ZIEL</h3>
    Aufbau der ersten Einkaufsgemeinschaft für LifeScience Labore, über die jeder Teilnehmer seinen Laborbedarf zu Großhandelspreisen decken kann. Das Kampagnenprinzip.<br>
    Wir bündeln den Jahresbedarf an Chemikalien, Verbrauchsmaterialien und Laborbedarf unserer Teilnehmer und begegnen Herstellern als gern gesehener Großabnehmer. Je mehr Teilnehmer mitmachen, desto größer unsere Verhandlungsmasse, desto besser unsere Einkaufspreise.
  </div>

  <svg class="abs info-icon" style="top:950px;" width="42" height="36" viewBox="0 0 42 36" fill="none" stroke="#173f6f" stroke-width="1.5">
    <path d="M14 6 V2 H28 V6"/><rect x="2" y="6" width="38" height="28" rx="3"/>
    <rect x="6" y="10" width="30" height="20" stroke-dasharray="1.5 1.5"/>
  </svg>
  <div class="abs info-rule" style="top:948px; height:67px;"></div>
  <div class="abs info" style="top:948px;">
    <h3>KEEP IT SIMPLE</h3>
    Wir verzichten auf Rahmenverträge, Mindestbestellmengen oder sonstigen Verpflichtungen! Ihr entscheidet: Gefallen euch die Preise, dann reservieren wir für euch euren Jahresbedarf und ihr kauft ganz regulär. Kauft ihr weniger ab? Kein Problem, der Einkaufsgemeinschaft entsteht hierdurch kein Schaden. Unsere Lieferanten sind absolut kundenorientiert und kulant.
  </div>

  <svg class="abs info-icon" style="left:155px; top:1054px;" width="32" height="36" viewBox="0 0 32 36" fill="none" stroke="#173f6f" stroke-width="1.5">
    <rect x="2" y="2" width="28" height="32"/><line x1="2" y1="8" x2="30" y2="8"/>
    <path d="M10 12 V17 a6 6 0 0 0 12 0 V12"/>
  </svg>
  <div class="abs info-rule" style="top:1054px; height:56px;"></div>
  <div class="abs info" style="top:1054px;">
    <h3>FAIRNESS</h3>
    Jeder Teilnehmer trägt entscheidend dazu bei, dass die Gemeinschaft optimale Preise erhält und wachsen kann. Deshalb gelten die Preise für alle, ganz unabhängig von (unverbindlich) angemeldeten Abnahmemengen.
  </div>

  <a class="abs cta cta-two" href="#">ICH MÖCHTE MEHR ERFAHREN</a>

  <div class="abs footer"></div>
  <div class="abs footer-text">Pipette Union e.K.<br>IMPRESSUM | DATENSCHUTZERKLÄRUNG</div>

</body>
</html>
```